Velnix Orbit Nine Toothbrush Backcard Design

We need a toothbrush backcard (toothbrush packaging) design for our new toothbrush. We are one of the leading toothbrush distributor and producer company. At the moment our toothbrushes are selling at Varno, Sunpeak Shop, Q-Ninety and many more supermarkets and mom-and-pop shops in Thailand. Our toothbrush is emphasized on the soft and slim tip bristles which will not hurt your enamel. Easy to grip handle that will ease of use. These 2 mains point should be communicated through the design.

Our brand name is Velnix (see attached logo that you can use) and the toothbrush model is Orbit Nine. We will have 2 series for this model which are Orbit Nine Extra Soft and Orbit Nine Medium soft. They are basically differentiated by its packaging colors.

We are looking for the attractive and outstanding design from what available in the market right now. Please see enclosed die cut shape of the packaging. This backcard will hold 3 pieces of toothbrush with clear blister cover.

P.S We are very confident that our product produced with very good quality that's why we want to attract people to try. So when they walk in the aisle we want our toothbrush packaging to be eye catching and welcome customer to try.

Target Market(s)

B+ household consumers age between 18-65 both men and women who has open minded to the new product and willing to spend money without brand royalty.

Font styles to use
Sans Serif

Colors

Designer to choose colors to be used in the design.

Requirements
Must have
• - Logo, and model name
• - Quality mark as following GMP, KRV, ISO9001:2015, ISO22176
• - Attractive character which attract the target clients to try.
• - 2-sided packaging using attached die cut
Nice to have
Should not have
• What other brands have

```html
<!DOCTYPE html>
<html lang="en">
<head>
<meta charset="utf-8">
<title>Velnix Orbit Nine Backcards</title>
<link rel="stylesheet" href="https://fonts.googleapis.com/css2?family=Poppins:wght@700&family=Lobster&family=Exo+2:ital,wght@1,800&family=Barlow+Condensed:wght@700&display=swap">
<style>
  :root {
    --page: #ffffff;
    --frame: #444444;
    --card: #050608;
    --blister: #3aa6d8;
    --logo-light: #ffffff;
    --logo-dark: #3b3b3b;
    --label: #fcf5d9;
    --tag: #f6c31c;
    --tag-text: #1e1e1e;
    --badge: #5b3f72;
    --ribbon-text: #ffffff;
  }
  html, body { margin: 0; padding: 0; overflow: hidden; background: var(--page); }
  .canvas { display: block; width: 844px; height: 1200px; }
  .page-frame { fill: none; stroke: var(--frame); stroke-width: 1; }
  .card-bg { fill: var(--card); }
  .blister-line { fill: none; stroke: var(--blister); stroke-width: 1.4; }
  .brand { font-family: "Poppins", sans-serif; font-weight: 700; text-anchor: middle; letter-spacing: 1px; }
  .brand--header { fill: var(--logo-light); font-size: 42px; }
  .brand--label { fill: var(--logo-dark); font-size: 44px; }
  .brand-dot { fill: var(--tag); }
  .label-panel { fill: var(--label); }
  .ribbon-copy { font-family: "Exo 2", sans-serif; font-style: italic; font-weight: 800; font-size: 14px; fill: var(--ribbon-text); text-anchor: end; }
  .ribbon-script { font-family: "Lobster", cursive; font-size: 64px; fill: var(--ribbon-text); }
  .pack-tag { fill: var(--tag); }
  .pack-text { font-family: "Exo 2", sans-serif; font-style: italic; font-weight: 800; font-size: 31px; fill: var(--tag-text); text-anchor: middle; }
  .badge-ring { fill: none; stroke: var(--badge); stroke-width: 2; }
  .badge-core { fill: var(--label); stroke: var(--badge); stroke-width: 2; }
  .badge-text { font-family: "Barlow Condensed", sans-serif; font-weight: 700; font-size: 8.4px; fill: #222; letter-spacing: 0.6px; }
</style>
</head>
<body>
<svg class="canvas" viewBox="0 0 800 1137" preserveAspectRatio="none" xmlns="http://www.w3.org/2000/svg" xmlns:xlink="http://www.w3.org/1999/xlink">
  <defs>
    <radialGradient id="glow-red" cx="0.45" cy="0.38" r="0.6">
      <stop offset="0" stop-color="#ff5a4a"/>
      <stop offset="0.25" stop-color="#d8140f"/>
      <stop offset="0.6" stop-color="#4a0304"/>
      <stop offset="1" stop-color="#050608"/>
    </radialGradient>
    <radialGradient id="glow-blue" cx="0.45" cy="0.38" r="0.6">
      <stop offset="0" stop-color="#7fd6ff"/>
      <stop offset="0.25" stop-color="#0f7fe0"/>
      <stop offset="0.6" stop-color="#03213f"/>
      <stop offset="1" stop-color="#050608"/>
    </radialGradient>
    <linearGradient id="brush-fill" x1="0" y1="0" x2="0" y2="1">
      <stop offset="0" stop-color="#ffffff" stop-opacity="0.85"/>
      <stop offset="0.4" stop-color="#f3f3f3" stop-opacity="0.45"/>
      <stop offset="0.45" stop-color="#9fe3cf" stop-opacity="0.55"/>
      <stop offset="1" stop-color="#e8f6f1" stop-opacity="0.8"/>
    </linearGradient>
    <linearGradient id="ribbon-red" x1="0" y1="0" x2="1" y2="0">
      <stop offset="0" stop-color="#8c1a1e"/>
      <stop offset="1" stop-color="#cf4a44"/>
    </linearGradient>
    <linearGradient id="ribbon-blue" x1="0" y1="0" x2="1" y2="0">
      <stop offset="0" stop-color="#1e3a78"/>
      <stop offset="1" stop-color="#25a9e6"/>
    </linearGradient>
    <path id="badge-arc" d="M -28 0 A 28 28 0 1 1 28 0 A 28 28 0 1 1 -28 0"/>
  </defs>

  <rect class="page-frame" x="0.5" y="0.5" width="799" height="1136"/>

  <!-- Extra Soft backcard -->
  <g class="backcard backcard--extra" transform="translate(22,33)">
    <rect class="card-bg" x="0" y="0" width="360" height="1072"/>
    <rect x="0" y="0" width="360" height="1072" fill="url(#glow-red)" role="img" aria-label="Red light glow background"/>
    <rect class="blister-line" x="25" y="17" width="314" height="1035" rx="30"/>
    <rect class="blister-line" x="45" y="45" width="278" height="982" rx="24"/>
    <rect class="blister-line" x="168" y="77" width="165" height="50" rx="16"/>
    <text class="brand brand--header" x="166" y="212">Velnix</text>
    <circle class="brand-dot" cx="252" cy="172" r="5"/>
    <rect x="58" y="227" width="250" height="820" rx="24" fill="url(#brush-fill)" role="img" aria-label="Three white toothbrushes with mint grip handles"/>
    <rect class="label-panel" x="58" y="582" width="262" height="360" rx="10"/>
    <text class="brand brand--label" x="188" y="670">Velnix</text>
    <circle class="brand-dot" cx="278" cy="630" r="5"/>
    <polygon points="28,708 322,696 332,760 38,774" fill="url(#ribbon-red)"/>
    <text class="ribbon-copy" x="160" y="738">Orbit Nine</text>
    <text class="ribbon-copy" x="160" y="755">Extra</text>
    <text class="ribbon-script" x="162" y="770">Soft</text>
    <polygon class="pack-tag" points="130,784 250,778 242,828 122,832"/>
    <text class="pack-text" x="186" y="818">3Pack</text>
    <g transform="translate(128,892)">
      <circle class="badge-ring" r="34"/>
      <circle class="badge-core" r="20"/>
      <text class="badge-text"><textPath xlink:href="#badge-arc" startOffset="4%">COMFORT GRIP HANDLE</textPath></text>
    </g>
    <g transform="translate(228,892)">
      <circle class="badge-ring" r="34"/>
      <circle class="badge-core" r="20"/>
      <text class="badge-text"><textPath xlink:href="#badge-arc" startOffset="2%">SOFT &amp; SLIM TIP BRISTLES</textPath></text>
    </g>
  </g>

  <!-- Medium Soft backcard -->
  <g class="backcard backcard--medium" transform="translate(403,33)">
    <rect class="card-bg" x="0" y="0" width="360" height="1072"/>
    <rect x="0" y="0" width="360" height="1072" fill="url(#glow-blue)" role="img" aria-label="Blue light glow background"/>
    <rect class="blister-line" x="25" y="17" width="314" height="1035" rx="30"/>
    <rect class="blister-line" x="45" y="45" width="278" height="982" rx="24"/>
    <rect class="blister-line" x="168" y="77" width="165" height="50" rx="16"/>
    <text class="brand brand--header" x="166" y="212">Velnix</text>
    <circle class="brand-dot" cx="252" cy="172" r="5"/>
    <rect x="58" y="227" width="250" height="820" rx="24" fill="url(#brush-fill)" role="img" aria-label="Three white toothbrushes with mint grip handles"/>
    <rect class="label-panel" x="58" y="582" width="262" height="360" rx="10"/>
    <text class="brand brand--label" x="188" y="670">Velnix</text>
    <circle class="brand-dot" cx="278" cy="630" r="5"/>
    <polygon points="28,708 322,696 332,760 38,774" fill="url(#ribbon-blue)"/>
    <text class="ribbon-copy" x="160" y="738">Orbit Nine</text>
    <text class="ribbon-copy" x="160" y="755">Medium</text>
    <text class="ribbon-script" x="162" y="770">Soft</text>
    <polygon class="pack-tag" points="130,784 250,778 242,828 122,832"/>
    <text class="pack-text" x="186" y="818">3Pack</text>
    <g transform="translate(128,892)">
      <circle class="badge-ring" r="34"/>
      <circle class="badge-core" r="20"/>
      <text class="badge-text"><textPath xlink:href="#badge-arc" startOffset="4%">COMFORT GRIP HANDLE</textPath></text>
    </g>
    <g transform="translate(228,892)">
      <circle class="badge-ring" r="34"/>
      <circle class="badge-core" r="20"/>
      <text class="badge-text"><textPath xlink:href="#badge-arc" startOffset="2%">SOFT &amp; SLIM TIP BRISTLES</textPath></text>
    </g>
  </g>
</svg>
</body>
</html>
```